I would like a single page website for Kestrel Lift Rentals. In the file list provided there is basic information to be included as well as our logo with colors, fonts and images to be included.
Site must be very simple and be able to be loaded onto smart phones etc very quickly.
Site needs to be very smart in appearance

Target Market(s)

All prospective drone customers from Police to Parties.

Industry/Entity Type

Hire

Coding

Coded - Design and coding required

Number of Pages Required

1 page

Requirements
Must have
• Must have variation of color schemes supplied
Nice to have
• Must be very eye catching without going over the top
Should not have
• Anything slow to load.

```html
<!DOCTYPE html>
<html lang="en">
<head>
<meta charset="utf-8">
<title>Kestrel Lift Rentals</title>
<link rel="stylesheet" href="https://fonts.googleapis.com/css2?family=Raleway:wght@300;400;500;600;700&display=swap">
<style>
  :root {
    --brand-green: #8cc63e;
    --icon-green: #6cbf3a;
    --accent-blue: #3ea6d8;
    --ink: #222222;
    --nav-ink: #666666;
    --muted: #a9a9a9;
    --rule: #e3e3e3;
    --white: #ffffff;
    --hero-dark: #1f201c;
  }
  * { box-sizing: border-box; margin: 0; padding: 0; }
  html, body { width: 1200px; height: 1000px; overflow: hidden; background: var(--white); }
  body { font-family: "Raleway", Arial, sans-serif; color: var(--ink); position: relative; }

  .site-header {
    position: absolute; top: 0; left: 0; width: 1200px; height: 100px;
    border-top: 1px solid #333; background: var(--white);
  }
  .brand {
    position: absolute; left: 32px; top: 36px;
    color: var(--brand-green); font-weight: 600; line-height: 1;
  }
  .brand-line-1 { display: block; font-size: 28px; letter-spacing: 0.5px; }
  .brand-line-2 { display: block; font-size: 15px; letter-spacing: 7px; margin-top: 4px; }
  .main-nav { position: absolute; right: 45px; top: 0; height: 100px; display: flex; }
  .main-nav a {
    position: relative; display: block; padding: 0 15px; line-height: 100px;
    font-size: 15px; color: var(--nav-ink); text-decoration: none;
  }
  .main-nav a.is-active { color: #444; }
  .main-nav a.is-active::before {
    content: ""; position: absolute; left: 0; right: 0; top: 0; height: 3px; background: var(--accent-blue);
  }

  .hero { position: absolute; top: 100px; left: 0; width: 1200px; height: 558px; overflow: hidden; }
  .hero-photo {
    position: absolute; inset: 0;
    background:
      radial-gradient(ellipse 260px 180px at 120px 520px, rgba(110,210,120,0.55), transparent 70%),
      radial-gradient(ellipse 340px 300px at 260px 230px, rgba(225,225,220,0.55), transparent 70%),
      radial-gradient(ellipse 500px 260px at 950px 470px, rgba(120,110,90,0.45), transparent 70%),
      linear-gradient(180deg, #262720 0%, #34342c 55%, #1b1b18 100%);
  }
  .hero-copy { position: absolute; left: 615px; top: 180px; width: 520px; color: var(--white); }
  .hero-title { font-size: 34px; font-weight: 700; line-height: 36px; text-transform: uppercase; }
  .hero-list { list-style: none; margin-top: 18px; font-size: 15px; }
  .hero-list li { line-height: 26px; }
  .hero-button {
    display: inline-block; margin-top: 20px; padding: 0 12px; height: 34px; line-height: 32px;
    background: var(--white); color: #333; font-size: 15px; border-radius: 2px;
    border-bottom: 3px solid #cfcfcf; text-decoration: none;
  }
  .slider-arrow {
    position: absolute; top: 245px; width: 70px; height: 70px; border-radius: 50%;
    background: rgba(20,20,18,0.75);
  }
  .slider-arrow svg { position: absolute; top: 27px; }
  .slider-prev { left: -35px; }
  .slider-prev svg { left: 42px; }
  .slider-next { right: -35px; }
  .slider-next svg { left: 16px; }
  .slider-progress { position: absolute; left: 0; bottom: 0; width: 686px; height: 3px; background: var(--accent-blue); }

  .services { position: absolute; top: 658px; left: 0; width: 1200px; height: 342px; }
  .services-title { position: absolute; top: 120px; width: 100%; text-align: center; font-size: 31px; font-weight: 600; }
  .services-rule { position: absolute; top: 174px; left: 30px; width: 1140px; height: 1px; background: var(--rule); }
  .service-grid { position: absolute; top: 194px; left: 15px; width: 1170px; display: flex; }
  .service { width: 292.5px; text-align: center; padding: 0 25px; }
  .service svg { display: block; margin: 0 auto; height: 58px; fill: var(--icon-green); }
  .service p { margin-top: 9px; font-size: 18px; font-weight: 300; color: var(--muted); line-height: 20px; }
</style>
</head>
<body>
  <header class="site-header">
    <div class="brand">
      <span class="brand-line-1">KESTREL LIFT</span>
      <span class="brand-line-2">RENTALS</span>
    </div>
    <nav class="main-nav">
      <a href="#" class="is-active">Home</a>
      <a href="#">Services</a>
      <a href="#">About</a>
      <a href="#">Contact</a>
    </nav>
  </header>

  <section class="hero">
    <div class="hero-photo" role="img" aria-label="White quadcopter drone with camera gimbal hovering against a dark, blurred background"></div>
    <div class="hero-copy">
      <h1 class="hero-title">4K Video Footage, 12MP Images</h1>
      <ul class="hero-list">
        <li>Construction project updates for remote stake holders</li>
        <li>Building/Roof Condition Inspections</li>
        <li>Lost pets</li>
        <li>Accident reconstructions</li>
        <li>Insurance assessing</li>
      </ul>
      <a href="#" class="hero-button">Read More</a>
    </div>
    <a href="#" class="slider-arrow slider-prev" aria-label="Previous slide">
      <svg width="12" height="16" viewBox="0 0 12 16"><path d="M10 1 L3 8 L10 15" fill="none" stroke="#fff" stroke-width="2.5"/></svg>
    </a>
    <a href="#" class="slider-arrow slider-next" aria-label="Next slide">
      <svg width="12" height="16" viewBox="0 0 12 16"><path d="M2 1 L9 8 L2 15" fill="none" stroke="#fff" stroke-width="2.5"/></svg>
    </a>
    <div class="slider-progress"></div>
  </section>

  <section class="services">
    <h2 class="services-title">Our Services</h2>
    <div class="services-rule"></div>
    <div class="service-grid">
      <div class="service">
        <svg viewBox="0 0 56 58" width="56" aria-hidden="true">
          <rect x="10" y="6" width="4" height="12"/><rect x="26" y="6" width="4" height="12"/><rect x="42" y="6" width="4" height="12"/>
          <circle cx="12" cy="3" r="2.5"/><circle cx="28" cy="3" r="2.5"/><circle cx="44" cy="3" r="2.5"/>
          <path d="M4 20 H52 V34 Q46 40 40 34 Q34 40 28 34 Q22 40 16 34 Q10 40 4 34 Z"/>
          <path d="M4 40 Q10 46 16 40 Q22 46 28 40 Q34 46 40 40 Q46 46 52 40 V54 H4 Z"/>
          <rect x="0" y="54" width="56" height="4"/>
        </svg>
        <p>Special Occasions, Children's Birthday Parties, Weddings</p>
      </div>
      <div class="service">
        <svg viewBox="0 0 54 58" width="54" aria-hidden="true">
          <path d="M12 2 H42 V20 Q42 36 27 38 Q12 36 12 20 Z"/>
          <path d="M12 6 H2 V14 Q2 26 14 28 L14 23 Q7 22 7 14 V11 H12 Z"/>
          <path d="M42 6 H52 V14 Q52 26 40 28 L40 23 Q47 22 47 14 V11 H42 Z"/>
          <rect x="23" y="36" width="8" height="10"/>
          <rect x="14" y="46" width="26" height="8"/>
        </svg>
        <p>Sporting events - 4K, Video of yourself participating in marathons etc</p>
      </div>
      <div class="service">
        <svg viewBox="0 0 60 58" width="60" aria-hidden="true">
          <path d="M30 0 L60 14 V18 H0 V14 Z"/>
          <rect x="3" y="20" width="54" height="4"/>
          <rect x="7" y="26" width="6" height="22"/><rect x="19" y="26" width="6" height="22"/>
          <rect x="35" y="26" width="6" height="22"/><rect x="47" y="26" width="6" height="22"/>
          <rect x="27" y="26" width="6" height="22" opacity="0"/>
          <rect x="3" y="50" width="54" height="3"/><rect x="0" y="54" width="60" height="4"/>
        </svg>
        <p>Real Estate Brochures</p>
      </div>
      <div class="service">
        <svg viewBox="0 0 56 58" width="56" aria-hidden="true">
          <rect x="8" y="0" width="12" height="10"/><rect x="36" y="0" width="12" height="10"/>
          <path d="M6 12 H22 V56 H0 V30 Z"/>
          <path d="M34 12 H50 L56 30 V56 H34 Z"/>
          <rect x="22" y="16" width="12" height="16"/>
        </svg>
        <p>Surveillance – Police, Local councils worksafe etc</p>
      </div>
    </div>
  </section>
</body>
</html>
```